Business Card Design

We need a new business card design for a company based in Ashgrove, OK. We provide business consulting services in the information technology / services space. We like variations of the color blue, aqua, black, light tan, and white. Would like "cool" tones. The design should clearly communicate professionalism. Think outside the box - we don't want something "typical". Our company name is "Vantrell Advisory, LLC".
Updates

Thank you all for your submissions. We have seen some very creative and inspired designs. We have made a decision and will be moving forward with that design. Appreciate all of the hard work.

Industry/Entity Type

Information Technology

Contact Information for Business Card

Denise Harlow Trumbey
482 West Maple Ridge Dr.
Ashgrove, OK 76185

```html
<!DOCTYPE html>
<html lang="en">
<head>
<meta charset="utf-8">
<title>Vantrell Advisory, LLC — Business Card</title>
<link rel="stylesheet" href="https://fonts.googleapis.com/css2?family=Questrial&family=Ubuntu:wght@400&family=Quicksand:wght@700&display=swap">
<style>
  :root {
    --backdrop: #3b3b3d;
    --card: #050505;
    --brand-blue: #1c86c6;
    --silver: #b8b8b8;
    --text-light: #d2d2d2;
  }
  html, body {
    margin: 0;
    width: 1200px;
    height: 800px;
    overflow: hidden;
    background: var(--backdrop);
  }
  .card {
    position: absolute;
    left: 100px;
    top: 114px;
    width: 1000px;
    height: 572px;
    background: var(--card);
    box-shadow: 0 18px 40px rgba(0,0,0,0.45);
  }
  .company-name {
    position: absolute;
    left: 62px;
    top: 92px;
    margin: 0;
    font-family: "Quicksand", sans-serif;
    font-weight: 700;
    font-size: 58px;
    letter-spacing: 1px;
    text-transform: uppercase;
    white-space: nowrap;
    color: var(--silver);
  }
  .person-name {
    position: absolute;
    left: 108px;
    top: 238px;
    margin: 0;
    font-family: "Ubuntu", sans-serif;
    font-weight: 400;
    font-size: 34px;
    letter-spacing: 1px;
    white-space: nowrap;
    color: var(--brand-blue);
  }
  .divider {
    position: absolute;
    left: 500px;
    top: 262px;
    width: 440px;
    height: 5px;
    background: var(--silver);
  }
  .address {
    position: absolute;
    right: 72px;
    top: 300px;
    margin: 0;
    font-family: "Questrial", sans-serif;
    font-style: normal;
    font-size: 26px;
    line-height: 34px;
    letter-spacing: 3px;
    text-align: right;
    white-space: nowrap;
    color: var(--text-light);
  }
  .address .pin { vertical-align: -4px; margin-right: 26px; }
  .contact {
    position: absolute;
    left: 128px;
    margin: 0;
    display: flex;
    align-items: center;
    gap: 22px;
    font-family: "Questrial", sans-serif;
    font-size: 27px;
    letter-spacing: 2px;
    white-space: nowrap;
    color: var(--text-light);
  }
  .contact-phone { top: 392px; }
  .contact-email { top: 458px; }
  .contact svg { flex: none; }
</style>
</head>
<body>
  <main class="card">
    <h1 class="company-name">Vantrell Advisory LLC</h1>
    <p class="person-name">Denise Harlow Trumbey</p>
    <div class="divider"></div>

    <address class="address">
      <svg class="pin" width="24" height="32" viewBox="0 0 24 32" aria-hidden="true">
        <path d="M12 1C6 1 1.5 5.5 1.5 11.2 1.5 18.5 12 31 12 31S22.5 18.5 22.5 11.2C22.5 5.5 18 1 12 1Z" fill="var(--brand-blue)"/>
        <circle cx="12" cy="11" r="4" fill="var(--card)"/>
      </svg>482<br>
      West Maple Ridge<br>
      Dr. Ashgrove,<br>
      OK 76185
    </address>

    <p class="contact contact-phone">
      <svg width="30" height="30" viewBox="0 0 24 24" aria-hidden="true">
        <path d="M6.6 10.8c1.4 2.8 3.8 5.1 6.6 6.6l2.2-2.2c.3-.3.7-.4 1-.2 1.1.4 2.3.6 3.6.6.6 0 1 .4 1 1V20c0 .6-.4 1-1 1C10.6 21 3 13.4 3 4c0-.6.4-1 1-1h3.5c.6 0 1 .4 1 1 0 1.3.2 2.5.6 3.6.1.3 0 .7-.2 1l-2.3 2.2Z" fill="var(--brand-blue)"/>
      </svg>
      817-364-2091
    </p>

    <p class="contact contact-email">
      <svg width="44" height="28" viewBox="0 0 44 28" aria-hidden="true">
        <rect x="1" y="1" width="42" height="26" fill="var(--brand-blue)"/>
        <path d="M1 1 22 16 43 1" fill="none" stroke="var(--card)" stroke-width="2"/>
        <path d="M1 27 17 12M43 27 27 12" fill="none" stroke="var(--card)" stroke-width="1.5"/>
      </svg>
      denise.trumbey@mailbox.com
    </p>
  </main>
</body>
</html>
```